Voltara Solutions Ltd - Project for new electric vehicle charging company

Please use Voltara Solutions Ltd logo & artwork instead of Brimwell.

We would like to produce a leaflet to advertise our electric vehicle charging company to build a reputation and workflow in the local area.

We would like to use the attached logo and maintain the colour palette of the of the logo to be simple, modern and effective.

I have over 15 years experience in the electrical industry and have direct access to the latest technology in electric vehicle charging.

All quotes to remain fixed costs subject to survey of the property and maintenance options can be available.

We can also offer further remedial works to any property through our sister company Brimwell Solutions Ltd.

Target Market(s)

Domestic / commercial customers

Requirements
Must have
• Voltara Solutions Ltd logo and colour palette.
Should not have
• Brimwell logo, Email or website address.

```html
<!DOCTYPE html>
<html lang="en">
<head>
<meta charset="UTF-8">
<title>Voltara Solutions Ltd – Leaflet</title>
<link href="https://fonts.googleapis.com/css2?family=Montserrat:wght@400;500;600;700;800&family=Roboto:wght@400&display=swap" rel="stylesheet">
<style>
  :root {
    --stage: #06a38f;
    --teal: #1db9a0;
    --teal-deep: #15a28c;
    --teal-ring: #129985;
    --charcoal: #2b2a2c;
    --white: #ffffff;
    --photo-light: #d9dde1;
    --photo-mid: #a9b0b8;
    --photo-dark: #4a5159;
  }
  * { box-sizing: border-box; margin: 0; padding: 0; }
  html, body {
    width: 1200px; height: 900px; overflow: hidden;
    background: var(--stage);
    font-family: "Montserrat", sans-serif;
  }
  .leaflet {
    position: absolute; left: 288px; top: 20px;
    width: 624px; height: 860px;
    overflow: hidden; background: var(--white);
    box-shadow: 0 8px 24px rgba(0,0,0,0.18);
  }
  .leaflet__backdrop { position: absolute; inset: 0; }

  .brand {
    position: absolute; left: 30px; top: 38px;
    display: flex; align-items: center; gap: 8px;
    z-index: 2;
  }
  .brand__mark {
    width: 36px; height: 36px; border-radius: 50%;
    border: 5px solid var(--teal);
  }
  .brand__name {
    color: var(--teal); font-weight: 500; font-size: 18px; letter-spacing: 0.1px;
    white-space: nowrap;
  }

  .hero-text { position: absolute; left: 36px; top: 198px; width: 250px; color: var(--white); }
  .hero-text__headline {
    color: var(--teal); font-weight: 800; font-size: 33px; line-height: 1.15;
  }
  .hero-text__sub { font-size: 16px; font-weight: 500; margin-top: 6px; }
  .hero-text__rule { width: 28px; height: 2px; background: var(--teal); margin: 12px 0 12px; }
  .hero-text__body { font-size: 9.5px; font-weight: 600; line-height: 1.55; }

  .offer { position: absolute; left: 0; top: 475px; width: 624px; color: var(--white); }
  .offer__title { text-align: center; font-size: 25px; font-weight: 800; letter-spacing: 0.3px; }
  .offer__rule {
    position: relative; width: 480px; height: 1px; margin: 8px auto 0;
    background: rgba(255,255,255,0.85);
  }
  .offer__rule::after {
    content: ""; position: absolute; left: 204px; top: -2px;
    width: 72px; height: 5px; background: var(--white);
  }
  .offer__intro {
    text-align: center; font-size: 12.5px; line-height: 1.55; margin: 12px auto 0; width: 500px;
  }

  .services {
    position: absolute; left: 36px; top: 590px; width: 560px;
    display: grid; grid-template-columns: 1fr 1fr; row-gap: 22px; column-gap: 16px;
    color: var(--white);
  }
  .service { display: flex; align-items: center; gap: 10px; }
  .service__icon { flex: 0 0 50px; width: 50px; height: 50px; }
  .service__title { font-size: 14.5px; font-weight: 700; }
  .service__text { font-size: 13px; line-height: 1.45; font-weight: 400; }

  .contact {
    position: absolute; left: 36px; top: 788px; width: 560px;
    border-top: 1px solid rgba(255,255,255,0.75);
    padding-top: 20px;
    display: flex; align-items: center; gap: 8px;
    color: var(--white); font-family: "Roboto", sans-serif; font-size: 12px;
    white-space: nowrap;
  }
  .contact__item { display: flex; align-items: center; gap: 6px; }
  .contact__sep { opacity: 0.9; }
  .contact__icon { width: 17px; height: 17px; }
</style>
</head>
<body>
<main class="leaflet">
  <svg class="leaflet__backdrop" width="624" height="860" viewBox="0 0 624 860">
    <defs>
      <linearGradient id="photoTone" x1="0" y1="0" x2="1" y2="1">
        <stop offset="0" stop-color="var(--photo-dark)"/>
        <stop offset="0.35" stop-color="var(--photo-light)"/>
        <stop offset="0.7" stop-color="var(--photo-mid)"/>
        <stop offset="1" stop-color="#5f7a93"/>
      </linearGradient>
      <linearGradient id="tealBand" x1="0" y1="0" x2="0" y2="1">
        <stop offset="0" stop-color="var(--teal)"/>
        <stop offset="1" stop-color="var(--teal-deep)"/>
      </linearGradient>
    </defs>
    <path class="teal-field" d="M0 330 L624 330 L624 860 L0 860 Z" fill="url(#tealBand)"/>
    <circle cx="166" cy="292" r="180" fill="var(--teal-ring)"/>
    <circle cx="162" cy="284" r="175" fill="var(--charcoal)"/>
    <circle cx="454" cy="206" r="214" fill="var(--teal-ring)"/>
    <circle cx="450" cy="200" r="210" fill="var(--white)"/>
    <circle cx="450" cy="200" r="204" fill="url(#photoTone)" role="img"
            aria-label="Photograph of an electric car plugged into a wall-mounted charging point"/>
  </svg>

  <div class="brand">
    <span class="brand__mark"></span>
    <span class="brand__name">Voltara Solutions Ltd</span>
  </div>

  <section class="hero-text">
    <h1 class="hero-text__headline">15 Years<br>Experience</h1>
    <p class="hero-text__sub">in the electrical industry</p>
    <div class="hero-text__rule"></div>
    <p class="hero-text__body">Proin ac leo quis odio ullamcorper egestas.<br>Nunc dictum ante eget aliquam aliquet.<br>Donec fermentum imperdiet pulvinar.</p>
  </section>

  <section class="offer">
    <h2 class="offer__title">What We Offer</h2>
    <div class="offer__rule"></div>
    <p class="offer__intro">Nunc aliquet enim eget enim consequat porta. Nullam porta metus sed lacus varius luctus. Fusce blandit urna nec tortor mollis mattis.</p>
  </section>

  <section class="services">
    <article class="service">
      <svg class="service__icon" viewBox="0 0 50 50" fill="none" stroke="#fff" stroke-width="1.5">
        <circle cx="25" cy="25" r="23"/>
        <path d="M14 31 l3-7 h16 l3 7 v4 h-22z M18 35v2 M32 35v2"/>
        <path d="M26 12 l-3 6 h4 l-3 6"/>
      </svg>
      <div><h3 class="service__title">Aenean at laoreet tellus</h3>
      <p class="service__text">Phasellus convallis, urna ut rhoncus rhoncus, sem tortor porttitor nulla.</p></div>
    </article>
    <article class="service">
      <svg class="service__icon" viewBox="0 0 50 50" fill="none" stroke="#fff" stroke-width="1.5">
        <circle cx="25" cy="25" r="23"/>
        <rect x="17" y="14" width="12" height="21" rx="1"/>
        <path d="M14 36h18 M29 20h4v10a2 2 0 0 0 4 0v-8"/>
        <path d="M24 18l-3 5h4l-3 5"/>
      </svg>
      <div><h3 class="service__title">Aenean at laoreet tellus</h3>
      <p class="service__text">Phasellus convallis, urna ut rhoncus rhoncus, sem tortor porttitor nulla.</p></div>
    </article>
    <article class="service">
      <svg class="service__icon" viewBox="0 0 50 50" fill="none" stroke="#fff" stroke-width="1.5">
        <circle cx="25" cy="25" r="23"/>
        <rect x="17" y="13" width="13" height="23" rx="1.5"/>
        <path d="M14 37h19 M30 22l4 3v7"/>
        <path d="M24 19l-3 5h4l-3 5"/>
      </svg>
      <div><h3 class="service__title">Aenean at laoreet tellus</h3>
      <p class="service__text">Phasellus convallis, urna ut rhoncus rhoncus, sem tortor porttitor nulla.</p></div>
    </article>
    <article class="service">
      <svg class="service__icon" viewBox="0 0 50 50" fill="none" stroke="#fff" stroke-width="1.5">
        <circle cx="25" cy="25" r="23"/>
        <rect x="15" y="14" width="14" height="18" rx="3"/>
        <path d="M29 22h4a2 2 0 0 1 2 2v8a3 3 0 0 1-6 0v-2 M22 32v4"/>
        <path d="M23 18l-3 5h4l-3 5"/>
      </svg>
      <div><h3 class="service__title">Aenean at laoreet tellus</h3>
      <p class="service__text">Phasellus convallis, urna ut rhoncus rhoncus, sem tortor porttitor nulla.</p></div>
    </article>
  </section>

  <footer class="contact">
    <span class="contact__item">
      <svg class="contact__icon" viewBox="0 0 20 20"><circle cx="10" cy="10" r="10" fill="#fff"/><path d="M6.5 5.5l2 0.3 0.8 2.2-1.2 1a6 6 0 0 0 3 3l1-1.2 2.2 0.8 0.3 2c-1 1-2.5 1.2-4 0.4a10 10 0 0 1-4.5-4.5c-0.8-1.5-0.6-3 0.4-4z" fill="var(--teal)"/></svg>
      0121-555-0147
    </span>
    <span class="contact__sep">|</span>
    <span class="contact__item">
      <svg class="contact__icon" viewBox="0 0 20 20"><circle cx="10" cy="10" r="10" fill="#fff"/><rect x="5" y="6.5" width="10" height="7" rx="1" fill="none" stroke="var(--teal)" stroke-width="1.3"/><path d="M5.5 7l4.5 3.5 4.5-3.5" fill="none" stroke="var(--teal)" stroke-width="1.3"/></svg>
      enquiries@voltara-solutions.com
    </span>
    <span class="contact__sep">|</span>
    <span class="contact__item">
      <svg class="contact__icon" viewBox="0 0 20 20"><circle cx="10" cy="10" r="10" fill="#fff"/><g fill="none" stroke="var(--teal)" stroke-width="1.1"><circle cx="10" cy="10" r="5.5"/><ellipse cx="10" cy="10" rx="2.4" ry="5.5"/><path d="M4.5 10h11 M5.5 7h9 M5.5 13h9"/></g></svg>
      www.voltara-solutions.co.uk
    </span>
  </footer>
</main>
</body>
</html>
```